Harold The Realtor Business Card Design

I need a new card design for my real estate business in Seattle Wa. I am interested in a unique design. My business revolves around my personal services and I want the card to show professionalism, creativity and good execution. I specialize in residential real estate in Maple ridge / downtown neighborhoods. The card is my first impression on may of my clients and in the service industry any time you can stand out from the crowd and make an impression will go a long way.

Target Market(s)

I will be handing the card to prospects/ potential buyers and sellers of residential real estate.

Industry/Entity Type

Real Estate Agent

Contact Information for Business Card

Email: Info@Haroldtherealtor.com Website: HaroldtheRealtor.com Cell phone: 206-555-0184 Fax 206-555-0127

Font styles to use
Sans Serif

Colors
0255a3
ffc214

Requirements
Must have
• I will need to have my firms logo "Keystone 8" and my logo "HTR" on the business card. I would like to have my firms logo smaller then mine. I would also like to have my photo on the card. By business colors are gold and white with blue accents.
Nice to have
• It would be nice to have a unique shape or feel (texture) rather then your standard business card. I saw cardly press had metal cards which could be interesting.

```html
<!DOCTYPE html>
<html lang="en">
<head>
<meta charset="utf-8">
<title>Harold The Realtor – Business Card</title>
<link rel="stylesheet" href="https://fonts.googleapis.com/css2?family=Lato:wght@400;700&display=swap">
<style>
  :root {
    --page: #f2f2f4;
    --navy-light: #2b3185;
    --navy-dark: #151a4e;
    --gold: #a8803f;
    --ink: #1d1d1f;
    --grey: #6b6b70;
    --rule: #e2e2e6;
    --white: #ffffff;
  }
  * { box-sizing: border-box; margin: 0; padding: 0; }
  html, body { width: 1200px; height: 1200px; overflow: hidden; }
  body { background: var(--page); position: relative; font-family: "Lato", sans-serif; }

  .card {
    position: absolute; left: 180px; width: 840px; height: 480px;
    border-radius: 6px; overflow: hidden;
    box-shadow: 0 10px 30px rgba(0,0,0,.12);
  }

  /* Front */
  .card--front {
    top: 90px;
    background: linear-gradient(160deg, var(--navy-light) 0%, var(--navy-dark) 100%);
    display: flex; align-items: center; justify-content: center;
  }
  .business-name {
    font-family: "Lato", sans-serif; font-weight: 700;
    text-align: center; line-height: 1.1; white-space: nowrap;
  }
  .card--front .business-name { font-size: 58px; color: var(--white); }

  /* Back */
  .card--back { top: 630px; background: var(--white); }
  .back-left {
    position: absolute; left: 0; top: 0; width: 390px; height: 458px;
    border-right: 2px solid var(--rule);
  }
  .card--back .business-name {
    position: absolute; left: 0; right: 0; top: 150px;
    font-size: 32px; color: var(--navy-light);
  }
  .firm-name {
    position: absolute; left: 0; right: 0; bottom: 50px; text-align: center;
    font-family: "Lato", sans-serif; font-weight: 400; font-size: 28px; color: var(--ink);
  }

  .back-right { position: absolute; left: 430px; top: 40px; width: 390px; }
  .portrait {
    width: 190px; height: 220px;
    background: linear-gradient(180deg, #cfcac4 0%, #3d3a45 60%, #1f2440 100%);
  }
  .agent-name {
    font-family: "Lato", sans-serif; font-weight: 700;
    font-size: 30px; color: var(--ink); margin-top: 14px; line-height: 1;
  }
  .agent-title { font-size: 17px; color: var(--grey); letter-spacing: .02em; margin-top: 4px; }
  .contacts { list-style: none; margin-top: 28px; font-size: 19px; color: var(--ink); }
  .contacts li { display: flex; align-items: center; gap: 10px; margin-bottom: 6px; }
  .contacts svg { width: 18px; height: 18px; flex: none; }
  .contacts .pair svg + span { margin-right: 14px; }
  .band { position: absolute; left: 0; right: 0; bottom: 0; height: 22px; background: var(--navy-light); }
</style>
</head>
<body>
  <section class="card card--front">
    <p class="business-name">Harold The Realtor</p>
  </section>

  <section class="card card--back">
    <div class="back-left">
      <p class="business-name">Harold The Realtor</p>
      <p class="firm-name">Keystone 8</p>
    </div>

    <div class="back-right">
      <div class="portrait" role="img" aria-label="Portrait photo of Harold, real estate agent"></div>
      <p class="agent-name">Harold</p>
      <p class="agent-title">REAL ESTATE AGENT</p>
      <ul class="contacts">
        <li class="pair">
          <svg viewBox="0 0 18 18" fill="none" stroke="#a8803f" stroke-width="1.6"><rect x="5" y="1.5" width="8" height="15" rx="1.5"/><line x1="8" y1="13.5" x2="10" y2="13.5"/></svg>
          <span>(206) 555-0184</span>
          <svg viewBox="0 0 18 18" fill="#a8803f"><rect x="2" y="7" width="14" height="8" rx="1"/><rect x="5" y="2" width="8" height="5" fill="none" stroke="#a8803f" stroke-width="1.5"/><rect x="5" y="10" width="8" height="1.5" fill="#fff"/></svg>
          <span>(206) 555-0127</span>
        </li>
        <li>
          <svg viewBox="0 0 18 18" fill="#a8803f"><path d="M1 4h16v11H1z"/><path d="M1 4l8 6 8-6" fill="none" stroke="#fff" stroke-width="1.4"/></svg>
          <span>Info@Haroldtherealtor.com</span>
        </li>
        <li>
          <svg viewBox="0 0 18 18" fill="none" stroke="#a8803f" stroke-width="1.3"><circle cx="9" cy="9" r="7.5"/><ellipse cx="9" cy="9" rx="3.3" ry="7.5"/><line x1="1.5" y1="9" x2="16.5" y2="9"/><line x1="3" y1="5" x2="15" y2="5"/><line x1="3" y1="13" x2="15" y2="13"/></svg>
          <span>HaroldtheRealtor.com</span>
        </li>
      </ul>
    </div>

    <div class="band"></div>
  </section>
</body>
</html>
```